Business Card Design

I need a bussiness card that have some picture of a van and lorry.
Updates

Hello I could ask you to print business cards and message to the home address?

Industry/Entity Type

Business

Contact Information for Business Card

K&W Haulage LTD
truck and vans fridge
drivers recruitment
k.w-haulage@mailbox-example.com
tel nr 07812450396

```html
<!DOCTYPE html>
<html lang="en">
<head>
<meta charset="utf-8">
<title>K&amp;W Haulage LTD – Business Card</title>
<link rel="stylesheet" href="https://fonts.googleapis.com/css2?family=Roboto+Condensed:wght@400;700&family=Open+Sans:wght@600&family=Russo+One&display=swap">
<style>
  :root {
    --page-bg: #e9e7e4;
    --card-bg: #ffffff;
    --ink-dark: #3d3d3f;
    --ink-black: #111111;
    --accent-orange: #f0572a;
    --accent-red: #d8321e;
    --tagline-red: #8a2a22;
    --photo-light: #f4f6f8;
    --photo-mid: #b9c3cc;
    --photo-dark: #5d6670;
  }
  * { box-sizing: border-box; margin: 0; padding: 0; }
  html, body {
    width: 1200px;
    height: 1200px;
    overflow: hidden;
    background: var(--page-bg);
  }
  .sheet {
    position: relative;
    width: 1200px;
    height: 1200px;
  }
  .card {
    position: absolute;
    left: 180px;
    width: 840px;
    height: 520px;
    background: var(--card-bg);
    box-shadow: 0 6px 18px rgba(0,0,0,0.18);
    overflow: hidden;
  }
  .card--front { top: 60px; }
  .card--back { top: 620px; }

  /* Brand lockup */
  .brand {
    position: absolute;
    display: flex;
    flex-direction: column;
    align-items: flex-start;
  }
  .brand__row {
    display: flex;
    align-items: center;
    gap: 14px;
  }
  .brand__dot {
    width: 30px;
    height: 30px;
    border-radius: 50%;
    background: var(--accent-orange);
    flex: none;
  }
  .brand__name {
    font-family: "Roboto Condensed", sans-serif;
    font-weight: 700;
    color: var(--ink-dark);
    text-transform: uppercase;
    letter-spacing: 0.5px;
    line-height: 1;
  }
  .brand__tagline {
    font-family: "Open Sans", sans-serif;
    font-weight: 600;
    color: var(--tagline-red);
    line-height: 1.2;
    margin-top: 4px;
  }

  .card--front .brand {
    left: 250px;
    top: 150px;
  }
  .card--front .brand__name { font-size: 46px; }
  .card--front .brand__tagline { font-size: 19px; }

  .slogan {
    position: absolute;
    left: 0;
    right: 0;
    top: 330px;
    text-align: center;
    font-family: "Russo One", sans-serif;
    font-size: 50px;
    letter-spacing: 3px;
    color: var(--accent-orange);
    font-style: italic;
    word-spacing: 30px;
  }

  /* Back side */
  .photo {
    position: absolute;
    inset: 0;
    background:
      radial-gradient(ellipse 60% 55% at 25% 45%, rgba(60,80,110,0.55), transparent 70%),
      radial-gradient(ellipse 40% 50% at 82% 78%, rgba(40,45,52,0.65), transparent 70%),
      linear-gradient(180deg, var(--photo-light) 0%, var(--photo-mid) 55%, var(--photo-dark) 100%);
  }
  .photo-fade {
    position: absolute;
    inset: 0;
    background: linear-gradient(90deg, rgba(255,255,255,0) 30%, rgba(255,255,255,0.85) 60%, rgba(255,255,255,0.2) 100%),
                linear-gradient(0deg, rgba(255,255,255,0.9) 0%, rgba(255,255,255,0) 32%);
  }
  .card--back .brand {
    right: 26px;
    top: 120px;
    align-items: flex-end;
  }
  .card--back .brand__name { font-size: 38px; }
  .card--back .brand__tagline { font-size: 16px; }

  .contact {
    position: absolute;
    left: 36px;
    bottom: 50px;
    list-style: none;
    font-family: "Roboto Condensed", sans-serif;
    font-size: 26px;
    color: var(--ink-black);
    text-transform: uppercase;
  }
  .contact__item {
    display: flex;
    align-items: center;
    gap: 18px;
    margin-top: 14px;
  }
  .contact__icon { width: 32px; height: 26px; flex: none; }
</style>
</head>
<body>
<main class="sheet">

  <section class="card card--front" aria-label="Business card front">
    <div class="brand">
      <div class="brand__row">
        <span class="brand__dot"></span>
        <span class="brand__name">K&amp;W Haulage LTD</span>
      </div>
      <span class="brand__tagline">truck and vans fridge drivers recruitment</span>
    </div>
    <p class="slogan">EXPRESS DELIVERY</p>
  </section>

  <section class="card card--back" aria-label="Business card back">
    <div class="photo" role="img" aria-label="Photograph of two delivery vans and a refrigerated lorry driving on a road with mountains and a city skyline behind"></div>
    <div class="photo-fade"></div>

    <div class="brand">
      <div class="brand__row">
        <span class="brand__dot"></span>
        <span class="brand__name">K&amp;W Haulage LTD</span>
      </div>
      <span class="brand__tagline">truck and vans fridge drivers recruitment</span>
    </div>

    <ul class="contact">
      <li class="contact__item">
        <svg class="contact__icon" viewBox="0 0 32 24" aria-hidden="true">
          <rect x="1" y="2" width="30" height="20" fill="#111"/>
          <path d="M1 2 L16 14 L31 2" fill="none" stroke="#fff" stroke-width="2"/>
        </svg>
        <span>k.w-haulage@mailbox-example.com</span>
      </li>
      <li class="contact__item">
        <svg class="contact__icon" viewBox="0 0 32 26" aria-hidden="true">
          <path d="M2 9 Q16 -1 30 9 L26 12 L22 9 L22 6 Q16 4 10 6 L10 9 L6 12 Z" fill="#111"/>
          <path d="M9 12 L23 12 L28 24 L4 24 Z" fill="#111"/>
          <circle cx="16" cy="18" r="3.5" fill="#fff"/>
        </svg>
        <span>07812450396</span>
      </li>
    </ul>
  </section>

</main>
</body>
</html>
```